Web Calculator design Housing Investment

We have a web calculator that needs to be fixed from a design perspective. The key tasks are:<br/>1. Selecting icons / pictures / colours for the various steps<br/>2. Designing navigation between calculator steps<br/>3. Making suggestions for chart design. The limitation is that the charts are all using the Plovik API (the same charts that Plovik Grids use).<br/><br/>There are four entry screens and then a result screen. See attached PDF for screenshots. You can see our website at https://ambertidefunds.com for our corporate colours and style.

Target Market(s)

Real Estate Investors

Industry/Entity Type

Financial Planning

Number of Pages Required

1 page

Font styles to use
Sans Serif
Other font styles liked:
• Ubuntu

Colors
86cae7
3176b5
0455a3
ffffff

Requirements
Must have
• New Icons
• Suggested design for navigation
• Suggested design for charts

```html
<!DOCTYPE html>
<html lang="en">
<head>
<meta charset="utf-8">
<title>Housing Investment Calculator</title>
<link rel="stylesheet" href="https://fonts.googleapis.com/css2?family=Poppins:ital,wght@0,400;0,500;1,500&display=swap">
<style>
  :root {
    --accent: #e8242b;
    --ink: #2b2b2b;
    --ink-soft: #3a3a3a;
    --track: #ffffff;
    --card: rgba(255, 255, 255, 0.82);
    --radio-off: #cfcfcf;
    --bg-top: #fbc9a6;
    --bg-mid: #f7d8dc;
    --bg-low: #e6c6f0;
    --bg-bottom: #b7a2ef;
  }
  * { box-sizing: border-box; margin: 0; padding: 0; }
  html, body { width: 1200px; height: 613px; overflow: hidden; }
  body {
    position: relative;
    font-family: "Poppins", sans-serif;
    color: var(--ink);
    background:
      radial-gradient(ellipse 60% 55% at 15% 10%, rgba(250, 178, 120, 0.55), transparent 70%),
      radial-gradient(ellipse 50% 50% at 95% 5%, rgba(248, 196, 110, 0.5), transparent 70%),
      radial-gradient(ellipse 55% 60% at 95% 95%, rgba(150, 120, 235, 0.6), transparent 70%),
      linear-gradient(180deg, var(--bg-top) 0%, var(--bg-mid) 42%, var(--bg-low) 72%, var(--bg-bottom) 100%);
  }
  .title {
    position: absolute; top: 42px; left: 0; width: 100%;
    text-align: center; font-size: 33px; font-weight: 500; font-style: italic;
    letter-spacing: 0.3px;
  }
  .title .initial { color: var(--accent); }
  .title-rule {
    position: absolute; top: 106px; left: 147px; width: 903px; height: 1px;
    background: rgba(232, 36, 43, 0.45);
  }
  .steps { position: absolute; top: 143px; left: 0; width: 100%; height: 90px; }
  .step {
    position: absolute; width: 200px; margin-left: -100px; text-align: center;
    font-size: 15.5px; font-weight: 500; color: var(--ink-soft);
  }
  .step svg { display: block; margin: 0 auto 14px; width: 56px; height: 50px; }
  .step.is-active { color: var(--accent); }
  .progress {
    position: absolute; top: 249px; left: 147px; width: 905px; height: 13px;
    background: var(--track); border-radius: 7px; overflow: hidden;
  }
  .progress-fill {
    width: 135px; height: 100%; border-radius: 7px;
    background: repeating-linear-gradient(-60deg, var(--accent) 0 5px, #f6a3a5 5px 7px);
  }
  .progress-marker { position: absolute; top: 238px; left: 276px; }
  .question {
    position: absolute; top: 290px; left: 0; width: 100%; text-align: center;
    font-size: 16px; color: var(--ink-soft);
  }
  .option {
    position: absolute; top: 332px; width: 199px; height: 171px;
    background: var(--card); border-radius: 3px;
  }
  .option-art { position: absolute; top: 14px; left: 42px; width: 115px; height: 110px; border-radius: 4px; }
  .option--unit .option-art { background: linear-gradient(180deg, #8ec3ea 0%, #4b8fd0 80%, #6bb54a 100%); }
  .option--property .option-art { background: linear-gradient(180deg, #d9d9d9 0%, #b9b9b9 60%, #f0c340 100%); }
  .option-label {
    position: absolute; top: 136px; left: 0; width: 100%;
    display: flex; justify-content: center; align-items: center; gap: 12px;
    font-size: 17px;
  }
  .radio { width: 18px; height: 18px; border-radius: 50%; background: var(--radio-off); }
  .radio.is-checked { background: #fff; border: 2px solid #e0e0e0; position: relative; }
  .radio.is-checked::after {
    content: ""; position: absolute; inset: 2px; border-radius: 50%; background: var(--accent);
  }
  .nav {
    position: absolute; top: 540px; left: 0; width: 100%;
    display: flex; justify-content: center; align-items: center; gap: 9px;
    font-size: 13.5px; color: var(--ink-soft);
  }
</style>
</head>
<body>
  <h1 class="title"><span class="initial">H</span>ousing <span class="initial">I</span>nvestment <span class="initial">C</span>alculator</h1>
  <div class="title-rule"></div>

  <div class="steps">
    <div class="step is-active" style="left:203px">
      <svg viewBox="0 0 56 50" fill="none" stroke="#e8242b" stroke-width="2">
        <rect x="3" y="24" width="22" height="22"/><path d="M1 26 14 16 27 26"/>
        <path d="M7 32h14M7 37h14M7 42h14"/>
        <path d="M25 46V22l16-14 14 14v24z"/><path d="M38 46V36h6v10"/>
        <rect x="30" y="26" width="6" height="6"/><rect x="45" y="26" width="6" height="6"/>
      </svg>Property Type</div>
    <div class="step" style="left:378px">
      <svg viewBox="0 0 56 50" fill="none" stroke="#2b2b2b" stroke-width="2">
        <ellipse cx="28" cy="44" rx="18" ry="4"/>
        <path d="M28 42C18 30 15 24 15 17a13 13 0 0 1 26 0c0 7-3 13-13 25z" fill="#2b2b2b"/>
        <path d="M21 19l7-6 7 6v6h-14z" fill="#fff" stroke="none"/>
      </svg>Property Location</div>
    <div class="step" style="left:579px">
      <svg viewBox="0 0 56 50" fill="none" stroke="#2b2b2b" stroke-width="2">
        <path d="M10 2h26l8 8v36H10z"/><path d="M19 18l8-7 8 7v8H19z"/>
        <path d="M16 33h12M16 39h10"/>
        <circle cx="38" cy="36" r="7"/><path d="M43 41l7 7"/>
      </svg>Property Valuation</div>
    <div class="step" style="left:801px">
      <svg viewBox="0 0 56 50" fill="none" stroke="#2b2b2b" stroke-width="2">
        <path d="M6 26 28 6l22 20"/><path d="M12 22v24h32V22"/>
        <path d="M16 40l8-8 6 5 12-12"/><path d="M36 25h6v6"/>
        <path d="M28 13v12M31 16h-5a2 2 0 0 0 0 4h4a2 2 0 0 1 0 4h-5"/>
      </svg>Your Property Forecast</div>
    <div class="step" style="left:993px">
      <svg viewBox="0 0 56 50" fill="none" stroke="#2b2b2b" stroke-width="2">
        <rect x="22" y="2" width="28" height="38"/><rect x="26" y="6" width="20" height="8"/>
        <path d="M28 20h4M36 20h4M44 20h2M28 26h4M36 26h4M28 32h4M36 32h4"/>
        <path d="M4 30 17 19l13 11"/><path d="M8 28v18h18V28"/><path d="M14 46v-8h6v8"/>
      </svg>Calculator</div>
  </div>

  <div class="progress"><div class="progress-fill"></div></div>
  <svg class="progress-marker" width="11" height="8" viewBox="0 0 11 8"><path d="M0 0h11L5.5 8z" fill="#e8242b"/></svg>

  <p class="question">What type of property would you like to compare ?</p>

  <div class="option option--unit" style="left:389px">
    <div class="option-art" role="img" aria-label="Illustration of a blue apartment building with trees"></div>
    <div class="option-label"><span class="radio is-checked"></span>Unit</div>
  </div>
  <div class="option option--property" style="left:611px">
    <div class="option-art" role="img" aria-label="Illustration of houses with a garage"></div>
    <div class="option-label"><span class="radio"></span>Property</div>
  </div>

  <nav class="nav">
    <span>Previous</span>
    <svg width="44" height="18" viewBox="0 0 44 18" fill="none" stroke="#3a3a3a" stroke-width="1.2">
      <rect x="0.6" y="0.6" width="20" height="16.8"/><rect x="23.4" y="0.6" width="20" height="16.8"/>
      <path d="M16 9H5M9 5 5 9l4 4M28 9h11M35 5l4 4-4 4"/>
    </svg>
    <span>Next</span>
  </nav>
</body>
</html>
```